promotional flyer for Valtera Gym

we are after a double sided a5 leaflet to promote our gym, this is to go out to the general public to entice them into getting membership.

gym membership is £30 per month

it should also include the offer of - if you present this leaflet then there will be no joining fee

some of the features of the gym include

strength machines
cardio machines
functional area
sprung floor mat area

Target Market(s)

Adults 16+ who want to go to the gym and workout

Industry/Entity Type

Gym

Font styles to use
Other font styles liked:
• montserrat Regular

Requirements
Must have
• Clean on brand design
• use images supplied by us
Nice to have
• focus on an inclusive experience as the gym will be advertised to everyone
• should also use our "fitter, stronger, Healthier"

```html
<!DOCTYPE html>
<html lang="en">
<head>
<meta charset="utf-8">
<title>Valtera Gym – Membership Flyer</title>
<link rel="stylesheet" href="https://fonts.googleapis.com/css2?family=Montserrat:wght@400;500;600;700;800;900&family=Varela+Round&display=swap">
<style>
  :root {
    --page-bg: #d6dde4;
    --slate: #4f5e6b;
    --slate-dark: #44515d;
    --slate-light: #64727e;
    --orange: #e8501f;
    --orange-deep: #c9411a;
    --orange-faint: #b63d17;
    --white: #ffffff;
    --ink: #2e3a45;
    --line: #7c8a96;
    --muted: #b7c0c8;
    --photo-a: #6b6560;
    --photo-b: #b7b3ae;
  }
  * { margin: 0; padding: 0; box-sizing: border-box; }
  html, body { width: 1013px; height: 1200px; overflow: hidden; background: var(--page-bg); }
  body { position: relative; font-family: "Montserrat", sans-serif; }

  .flyer {
    position: absolute; left: 96px; top: 18px;
    width: 1273px; height: 1805px;
    transform: scale(0.6443); transform-origin: top left;
    overflow: hidden; background: var(--slate);
  }
  .flyer-shapes { position: absolute; inset: 0; }

  .brand { position: absolute; left: 860px; top: 112px; width: 400px; text-align: center; color: var(--slate-dark); }
  .brand-name { font-family: "Montserrat", sans-serif; font-weight: 500; font-size: 40px; letter-spacing: 2px; display: inline-flex; align-items: center; gap: 14px; }
  .brand-dot { width: 22px; height: 22px; border-radius: 50%; background: var(--orange); display: inline-block; }
  .brand-tagline { margin-top: 8px; font-size: 14px; font-weight: 600; letter-spacing: 2px; color: var(--orange); }

  .slogan { position: absolute; right: 30px; top: 618px; text-align: right; color: var(--white); font-weight: 600; font-size: 70px; line-height: 91px; letter-spacing: 3px; }

  .audience { position: absolute; left: 457px; top: 930px; color: var(--white); }
  .audience-age { font-weight: 900; font-size: 112px; line-height: 96px; }
  .audience-title { font-weight: 900; font-size: 92px; line-height: 86px; letter-spacing: 2px; }
  .audience-text { font-weight: 400; font-size: 36px; line-height: 40px; margin-top: 6px; }

  .features-pill {
    position: absolute; left: 354px; top: 1205px; width: 500px; height: 90px;
    background: var(--white); border: 5px solid var(--orange-deep); border-left: none;
    border-radius: 0 45px 45px 0; display: flex; align-items: center; justify-content: center;
    box-shadow: 0 6px 10px rgba(0,0,0,0.2);
  }
  .features-title { font-weight: 800; font-size: 52px; letter-spacing: 3px; color: var(--ink); padding-left: 110px; }

  .feature-list { position: absolute; left: 450px; top: 1328px; list-style: none; color: var(--white); }
  .feature-list li { display: flex; align-items: center; gap: 18px; font-weight: 600; font-size: 36px; height: 67px; }
  .feature-list svg { width: 24px; height: 24px; }

  .photo-circle { position: absolute; width: 320px; height: 320px; border-radius: 50%; background: var(--orange); display: flex; align-items: center; justify-content: center; box-shadow: 0 4px 10px rgba(0,0,0,0.25); }
  .photo-circle .photo { width: 290px; height: 290px; border-radius: 50%; border: 6px solid var(--white); }
  .photo-circle.one { left: 110px; top: 912px; }
  .photo-circle.one .photo { background: radial-gradient(circle at 50% 40%, #8d6f66, #3f3a3c 75%); }
  .photo-circle.two { left: 110px; top: 1192px; }
  .photo-circle.two .photo { background: radial-gradient(circle at 45% 40%, #7b5a68, #3a3040 70%); }
  .photo-circle.three { left: 110px; top: 1472px; }
  .photo-circle.three .photo { background: radial-gradient(circle at 50% 35%, #6d6970, #2f3036 75%); }

  .offer-tag {
    position: absolute; left: 930px; top: 1158px; width: 195px; height: 320px;
    transform: rotate(8deg); text-align: center; font-family: "Varela Round", sans-serif; color: var(--ink);
  }
  .offer-tag-body { position: absolute; inset: 0; background: var(--white); clip-path: polygon(50% 0, 100% 22%, 100% 100%, 0 100%, 0 22%); border-radius: 0 0 14px 14px; }
  .offer-tag-hole { position: absolute; left: 83px; top: 32px; width: 28px; height: 28px; border-radius: 50%; background: var(--orange); border: 4px solid var(--slate-dark); }
  .offer-tag-text { position: absolute; left: 0; right: 0; top: 82px; font-size: 24px; line-height: 27px; font-weight: 700; }
  .offer-tag-text .lead { font-size: 34px; line-height: 38px; }
  .offer-tag-no { position: absolute; left: 0; right: 0; top: 194px; font-family: "Montserrat", sans-serif; font-weight: 900; font-size: 96px; line-height: 84px; color: var(--slate-dark); }
  .offer-tag-fee { position: absolute; left: 0; right: 0; bottom: 0; height: 46px; background: var(--slate-dark); color: var(--white); font-size: 23px; line-height: 46px; border-radius: 0 0 14px 14px; }

  .fitness-word {
    position: absolute; left: 490px; top: 1574px;
    font-weight: 700; font-size: 120px; line-height: 120px; letter-spacing: -2px;
    color: var(--orange-faint); opacity: 0.75; white-space: nowrap;
    transform: scaleX(0.7); transform-origin: left top;
  }

  .price { position: absolute; left: 880px; right: 30px; top: 0; height: 1805px; color: var(--white); text-align: right; }
  .price > div { position: absolute; right: 0; white-space: nowrap; }
  .price-amount { top: 1518px; font-weight: 600; font-size: 56px; line-height: 60px; }
  .price-amount sup { font-size: 28px; vertical-align: 20px; }
  .price-gym { top: 1566px; font-weight: 800; font-size: 120px; line-height: 100px; letter-spacing: 8px; margin-right: -8px; }
  .price-membership { top: 1655px; font-weight: 600; font-size: 37px; line-height: 40px; letter-spacing: 4px; margin-right: -4px; }
  .price-period { top: 1697px; font-weight: 400; font-size: 37px; line-height: 40px; letter-spacing: 5px; margin-right: -5px; color: var(--muted); }

  .contact { position: absolute; left: 464px; top: 1710px; list-style: none; color: var(--white); }
  .contact li { display: flex; align-items: center; gap: 18px; font-size: 20px; font-weight: 600; letter-spacing: 2px; height: 41px; }
  .contact svg { width: 20px; height: 20px; }

  .call-now { position: absolute; left: 30px; top: 1772px; transform: rotate(-90deg); transform-origin: top left; white-space: nowrap; color: var(--white); font-size: 50px; font-weight: 500; letter-spacing: 3px; line-height: 60px; }
  .call-now span { color: #aeb8c1; }
</style>
</head>
<body>
<main class="flyer">
  <svg class="flyer-shapes" viewBox="0 0 1273 1805" width="1273" height="1805">
    <defs>
      <linearGradient id="heroTone" x1="0" y1="0" x2="1" y2="1">
        <stop offset="0" stop-color="#3b3a3c"/>
        <stop offset="0.5" stop-color="#6b6560"/>
        <stop offset="1" stop-color="#b7b3ae"/>
      </linearGradient>
    </defs>
    <rect class="hero-photo" x="0" y="0" width="1273" height="990" fill="url(#heroTone)" role="img" aria-label="Photo of a woman doing a seated dumbbell shoulder press in the gym"/>
    <polygon points="0,480 390,730 0,985" fill="var(--slate)"/>
    <polygon points="640,891 1273,345 1273,1215" fill="var(--slate)"/>
    <polygon points="1000,880 1250,660 1250,1100" fill="none" stroke="var(--slate-light)" stroke-width="3" opacity="0.6"/>
    <polygon points="0,985 311,725 1273,1210 1273,1700 0,1700" fill="var(--orange)"/>
    <polygon points="0,1040 240,865 240,1805 0,1805" fill="var(--slate)"/>
    <rect x="0" y="1000" width="92" height="805" fill="var(--slate-light)"/>
    <rect x="0" y="1695" width="1273" height="110" fill="var(--slate-dark)"/>
    <rect x="150" y="1793" width="220" height="12" fill="var(--orange)"/>
    <polyline points="0,985 311,725 1273,1210" fill="none" stroke="#1e1e1e" stroke-width="4"/>
    <polyline points="0,480 635,812 1273,300" fill="none" stroke="var(--line)" stroke-width="4"/>
    <polygon points="815,150 1000,-20 1273,180 1273,190 1058,330" fill="var(--slate-dark)"/>
    <polygon points="825,125 1000,-30 1273,170 1273,175 1058,315" fill="var(--white)"/>
    <g class="social-markers" fill="var(--white)">
      <polygon points="38,582 88,620 38,658"/>
      <polygon points="38,672 88,710 38,748"/>
      <polygon points="38,762 88,800 38,838"/>
    </g>
  </svg>

  <div class="brand">
    <div class="brand-name"><span class="brand-dot"></span>VALTERA GYM</div>
    <div class="brand-tagline">FITTER &nbsp;|&nbsp; STRONGER &nbsp;|&nbsp; HEALTHIER</div>
  </div>

  <div class="slogan">FITTER<br>STRONGER<br>HEALTHIER</div>

  <div class="call-now"><span>CALL NOW - </span>555 0192 7781</div>

  <div class="photo-circle one"><div class="photo" role="img" aria-label="Photo of a member using a chest press machine"></div></div>
  <div class="photo-circle two"><div class="photo" role="img" aria-label="Photo of a member on a leg machine"></div></div>
  <div class="photo-circle three"><div class="photo" role="img" aria-label="Photo of a member on an exercise bike"></div></div>

  <div class="audience">
    <div class="audience-age">16+</div>
    <div class="audience-title">Adults</div>
    <div class="audience-text">Who want to go to<br>the gym and workout</div>
  </div>

  <div class="features-pill"><span class="features-title">FEATURES</span></div>

  <ul class="feature-list">
    <li><svg viewBox="0 0 24 24" fill="none" stroke="#fff" stroke-width="2.4"><circle cx="11" cy="13" r="9"/><path d="M7 13l4 4 11-13"/></svg>Strength machines</li>
    <li><svg viewBox="0 0 24 24" fill="none" stroke="#fff" stroke-width="2.4"><circle cx="11" cy="13" r="9"/><path d="M7 13l4 4 11-13"/></svg>Cardio machines</li>
    <li><svg viewBox="0 0 24 24" fill="none" stroke="#fff" stroke-width="2.4"><circle cx="11" cy="13" r="9"/><path d="M7 13l4 4 11-13"/></svg>Functional area</li>
    <li><svg viewBox="0 0 24 24" fill="none" stroke="#fff" stroke-width="2.4"><circle cx="11" cy="13" r="9"/><path d="M7 13l4 4 11-13"/></svg>Sprung floor mat area</li>
  </ul>

  <div class="offer-tag">
    <div class="offer-tag-body"></div>
    <div class="offer-tag-hole"></div>
    <div class="offer-tag-text"><span class="lead">If you</span><br>present this<br>leaflet then<br>there will be</div>
    <div class="offer-tag-no">NO</div>
    <div class="offer-tag-fee">JOINING FEE</div>
  </div>

  <div class="fitness-word">FITNESS</div>

  <div class="price">
    <div class="price-amount"><sup>£</sup>30</div>
    <div class="price-gym">GYM</div>
    <div class="price-membership">MEMBERSHIP</div>
    <div class="price-period">PER MONTH</div>
  </div>

  <ul class="contact">
    <li><svg viewBox="0 0 20 20" fill="none" stroke="#fff" stroke-width="1.6"><circle cx="10" cy="10" r="8.5"/><ellipse cx="10" cy="10" rx="4" ry="8.5"/><path d="M1.5 10h17M3 5.5h14M3 14.5h14"/></svg>www.valteragym.co.uk</li>
    <li><svg viewBox="0 0 20 20" fill="none" stroke="#fff" stroke-width="1.6"><rect x="1.5" y="4" width="17" height="12"/><path d="M1.5 4l8.5 7 8.5-7"/></svg>hello@valteragym.co.uk</li>
  </ul>
</main>
</body>
</html>
```